Brantwell Group needs a business card design

We need a new business card design using the logo recently selected in a logo competition on Pixel Forum. Our business is a consultancy specializing in aviation and energy and the winning business card design will promote an image of precision and professionalism with creativity.

Please use the logo with the name on the front of the card and use a complementary font. Make the back white with either the light grey or dark grey logo.

Target Market(s)

Senior finance and legal leaders at aviation and energy companies

Industry/Entity Type

Management Consulting

Contact Information for Business Card

Peter Haldane
President
Brantwell Group

www.brantwellgroup.example

(555) 304-6198
ph@brantwellgroup.example

Requirements
Must have
• Professional font that goes well with the logo font

```html
<!DOCTYPE html>
<html lang="en">
<head>
<meta charset="utf-8">
<title>Brantwell Group – Business Card</title>
<link rel="stylesheet" href="https://fonts.googleapis.com/css2?family=Quicksand:wght@300;400;500&family=Libre+Baskerville:wght@700&display=swap">
<style>
  :root {
    --card-bg: #ffffff;
    --ink: #1e1e1e;
    --ink-soft: #2a2a2a;
    --accent-lavender: #cccbdc;
    --icon-tile: #333333;
    --icon-letter: #ffffff;
  }

  * { margin: 0; padding: 0; box-sizing: border-box; }

  html, body {
    width: 1200px;
    height: 700px;
    overflow: hidden;
    background: var(--card-bg);
  }

  .card {
    position: relative;
    width: 1200px;
    height: 700px;
    background: var(--card-bg);
    font-family: "Quicksand", sans-serif;
    color: var(--ink);
  }

  .brand-name {
    position: absolute;
    right: 80px;
    top: 130px;
    font-family: "Quicksand", sans-serif;
    font-weight: 500;
    font-size: 58px;
    letter-spacing: 1px;
    color: var(--accent-lavender);
    white-space: nowrap;
  }

  .identity {
    position: absolute;
    left: 62px;
    top: 296px;
    width: 476px;
    text-align: center;
  }

  .identity__name {
    font-weight: 300;
    font-size: 50px;
    letter-spacing: 3px;
    line-height: 1;
    text-transform: uppercase;
    white-space: nowrap;
  }

  .identity__title {
    margin-top: 20px;
    font-weight: 400;
    font-size: 32px;
    letter-spacing: 1px;
    line-height: 1;
    text-transform: uppercase;
  }

  .contact-rail {
    position: absolute;
    left: 594px;
    top: 380px;
    width: 44px;
    height: 320px;
    background: var(--accent-lavender);
  }

  .contact-list {
    position: absolute;
    left: 587px;
    top: 0;
    list-style: none;
  }

  .contact-item {
    position: absolute;
    left: 0;
    display: flex;
    align-items: center;
    white-space: nowrap;
  }

  .contact-item--phone { top: 423px; }
  .contact-item--web   { top: 503px; }
  .contact-item--email { top: 583px; }

  .contact-item__icon {
    width: 28px;
    height: 34px;
    display: flex;
    align-items: center;
    justify-content: center;
    background: var(--icon-tile);
    color: var(--icon-letter);
    font-family: "Libre Baskerville", serif;
    font-weight: 700;
    font-size: 24px;
    line-height: 1;
    padding-bottom: 4px;
  }

  .contact-item--web .contact-item__icon { width: 30px; }

  .contact-item__text {
    margin-left: 22px;
    font-weight: 400;
    font-size: 25px;
    letter-spacing: 1.2px;
    color: var(--ink-soft);
  }

  .contact-item--web .contact-item__text { letter-spacing: 2.4px; }
</style>
</head>
<body>
  <main class="card">
    <div class="brand-name">Brantwell Group</div>

    <section class="identity">
      <h1 class="identity__name">Peter Haldane</h1>
      <p class="identity__title">President</p>
    </section>

    <div class="contact-rail" aria-hidden="true"></div>

    <ul class="contact-list">
      <li class="contact-item contact-item--phone">
        <span class="contact-item__icon" aria-hidden="true">p</span>
        <span class="contact-item__text">(555) 304-6198</span>
      </li>
      <li class="contact-item contact-item--web">
        <span class="contact-item__icon" aria-hidden="true">w</span>
        <span class="contact-item__text">www.brantwellgroup.example</span>
      </li>
      <li class="contact-item contact-item--email">
        <span class="contact-item__icon" aria-hidden="true">e</span>
        <span class="contact-item__text">ph@brantwellgroup.example</span>
      </li>
    </ul>
  </main>
</body>
</html>
```